Data Management as a Service Powerpoint Design

We need the attached PowerPoint presentation redesigning including all graphics, icons, images, and graphs. The messaging in the content should remain however artistic flair can be used to change any diagram/icon/graph layout.
For preferred colour scheme and brand continuity our website is: tavexo.com, however we are open to new colours/scheme.
The only stipulation is that the hexagon layout on the DMaaS product slide (slide 4) must remain. All other icons must be changed. We would also like this to be editable, and not full-slide static images pasted from another graphics suite.

```html
<!DOCTYPE html>
<html lang="en">
<head>
<meta charset="utf-8">
<title>Data Management as a Service – Slide Deck</title>
<link href="https://fonts.googleapis.com/css2?family=Montserrat:wght@300;400;700&family=Roboto:wght@300;400;500;700&display=swap" rel="stylesheet">
<style>
:root{
  --teal:#45adb8;
  --teal-dark:#2f8f9b;
  --navy:#1b3240;
  --orange:#e8733a;
  --ink:#222;
  --grey:#6b6b6b;
  --line:#d7e4e6;
  --panel:#f1f2f3;
  --canvas:#e8e9ea;
  --placeholder:#e9edee;
}
*{margin:0;padding:0;box-sizing:border-box}
html,body{width:1200px;height:1140px;overflow:hidden;background:var(--canvas)}
.deck{position:relative;width:1200px;height:1140px;font-family:Roboto,sans-serif}
.slide{position:absolute;width:381px;height:217px;background:#fff;overflow:hidden}
.art{position:absolute;left:0;top:0;width:381px;height:217px}
.slide-title{position:absolute;left:20px;top:8px;font:700 11.5px Roboto,sans-serif;color:var(--teal)}
.slide-title::after{content:"";position:absolute;left:-20px;top:17px;width:36px;height:1px;background:var(--orange)}
.brand{position:absolute;right:18px;top:9px;font:700 10.5px Montserrat,sans-serif;letter-spacing:1.6px;color:var(--ink)}
.footer{position:absolute;left:0;bottom:0;width:100%;height:9px;background:var(--teal);color:#fff;font:300 4px Roboto,sans-serif;padding-left:20px;line-height:9px}
.footer .page{position:absolute;right:17px;top:0;height:9px;padding:0 4px;background:var(--orange)}
.cover .title{position:absolute;left:23px;top:58px;font:400 18px/21px Montserrat,sans-serif;color:#fff}
.cover .date{position:absolute;left:25px;top:126px;width:56px;height:11px;border-radius:6px;background:var(--orange);color:#fff;font:400 5.5px/11px Roboto,sans-serif;text-align:center}
.cover .brand{top:auto;bottom:9px;right:16px;font-size:13px}
.s{font-family:Roboto,sans-serif}
.lbl{font:400 5px Roboto,sans-serif;fill:var(--grey)}
.tiny{font:400 3.2px Roboto,sans-serif;fill:var(--grey)}
.org{fill:var(--orange)}
.tl{fill:var(--teal)}
.hex-soft{fill:#fff;stroke:var(--line);stroke-width:1}
.ic{color:#8a8a8a}
.doc-placeholder{fill:var(--placeholder)}
.thanks{background:var(--teal)}
.thanks .big{position:absolute;left:0;width:100%;top:68px;text-align:center;font:300 36px Montserrat,sans-serif;color:#fff}
.thanks .pill{position:absolute;left:135px;top:156px;width:110px;height:26px;border-radius:13px;background:#fff;text-align:center;font:700 15px/26px Montserrat,sans-serif;letter-spacing:2px;color:var(--ink)}
.contacts{position:absolute;left:0;top:194px;width:100%;display:flex;justify-content:center;gap:14px;font:400 4.5px Roboto,sans-serif;color:#555}
.contacts span::before{content:"";display:inline-block;width:4px;height:4px;border-radius:50%;background:var(--orange);margin-right:2px;vertical-align:-0.5px}
</style>
</head>
<body>
<div class="deck">

<svg width="0" height="0" style="position:absolute">
  <defs>
    <linearGradient id="coverGrad" x1="0" y1="0" x2="1" y2="0.4">
      <stop offset="0" stop-color="#3aa7b4"/>
      <stop offset="0.55" stop-color="#23586a"/>
      <stop offset="1" stop-color="#172c39"/>
    </linearGradient>
    <linearGradient id="reportDark" x1="0" y1="0" x2="1" y2="0">
      <stop offset="0" stop-color="#2a2a2a"/>
      <stop offset="0.28" stop-color="#3a3a3a"/>
      <stop offset="0.3" stop-color="#f4f1f1"/>
      <stop offset="1" stop-color="#efe6e6"/>
    </linearGradient>
    <symbol id="hx" viewBox="-1 -1 2 2" overflow="visible"><polygon vector-effect="non-scaling-stroke" points="-1,0 -0.5,-0.866 0.5,-0.866 1,0 0.5,0.866 -0.5,0.866"/></symbol>
    <symbol id="hp" viewBox="-1 -1 2 2" overflow="visible"><polygon vector-effect="non-scaling-stroke" points="0,-1 0.866,-0.5 0.866,0.5 0,1 -0.866,0.5 -0.866,-0.5"/></symbol>
    <symbol id="i-monitor" viewBox="0 0 20 20"><g fill="none" stroke="currentColor" stroke-width="1"><rect x="2" y="3" width="16" height="11"/><path d="M10 14v3M6 17h8M5 6h6M5 9h8M5 11h4"/></g></symbol>
    <symbol id="i-gear" viewBox="0 0 20 20"><g fill="none" stroke="currentColor"><circle cx="10" cy="10" r="6" stroke-width="2.4" stroke-dasharray="2 1.6"/><circle cx="10" cy="10" r="2.2" stroke-width="1"/></g></symbol>
    <symbol id="i-db" viewBox="0 0 20 20"><g fill="none" stroke="currentColor" stroke-width="1"><ellipse cx="10" cy="4" rx="6" ry="2"/><path d="M4 4v12a6 2 0 0 0 12 0V4M4 8a6 2 0 0 0 12 0M4 12a6 2 0 0 0 12 0"/></g></symbol>
    <symbol id="i-cloud" viewBox="0 0 20 20"><path fill="none" stroke="currentColor" stroke-width="1" d="M5 15h10a3.6 3.6 0 0 0 0-7.2 5 5 0 0 0-9.4 1A3.2 3.2 0 0 0 5 15z"/></symbol>
    <symbol id="i-doc" viewBox="0 0 20 20"><g fill="none" stroke="currentColor" stroke-width="1"><path d="M5 2h7l4 4v12H5zM12 2v4h4M7 9h7M7 12h7M7 15h5"/></g></symbol>
    <symbol id="i-user" viewBox="0 0 20 20"><g fill="none" stroke="currentColor" stroke-width="1"><circle cx="10" cy="7" r="3.4"/><path d="M3.5 18a6.5 6.5 0 0 1 13 0z"/></g></symbol>
    <symbol id="i-search" viewBox="0 0 20 20"><g fill="none" stroke="currentColor" stroke-width="1.2"><circle cx="8.5" cy="8.5" r="5.5"/><path d="M12.6 12.6l5 5"/></g></symbol>
    <symbol id="i-export" viewBox="0 0 20 20"><g fill="none" stroke="currentColor" stroke-width="1"><path d="M5 2h8l3 3v13H5z"/><path d="M10.5 6v8M7.5 11l3 3 3-3"/></g></symbol>
    <symbol id="i-sync" viewBox="0 0 20 20"><g fill="none" stroke="currentColor" stroke-width="1.1"><path d="M16 8a6.4 6.4 0 0 0-11.6-1M4 12a6.4 6.4 0 0 0 11.6 1"/><path d="M3.6 3.6v3.6h3.6M16.4 16.4v-3.6h-3.6"/></g></symbol>
    <symbol id="i-in" viewBox="0 0 20 20"><g fill="none" stroke="currentColor" stroke-width="1.1"><path d="M11 3h5v14h-5M2 10h10M8.5 6.5L12 10l-3.5 3.5"/></g></symbol>
    <symbol id="i-ai" viewBox="0 0 20 20"><g fill="none" stroke="currentColor" stroke-width="1"><circle cx="10" cy="10" r="7"/><circle cx="7" cy="8" r="1.4"/><circle cx="13" cy="7" r="1.4"/><circle cx="12" cy="13" r="1.4"/><circle cx="7" cy="13" r="1.4"/><path d="M8.3 8.2l3.3-.9M12.6 8.3l-.4 3.4M10.6 13H8.4M7 9.4v2.2"/></g></symbol>
    <symbol id="i-bldg" viewBox="0 0 20 20"><g fill="none" stroke="currentColor" stroke-width="1"><path d="M3 18V6h6V2h8v16zM1 18h18"/><path d="M5 9h2M5 12h2M5 15h2M11 5h2M14 5h2M11 8h2M14 8h2M11 11h2M14 11h2M11 14h2M14 14h2"/></g></symbol>
    <symbol id="i-chart" viewBox="0 0 20 20"><g fill="none" stroke="currentColor" stroke-width="1"><rect x="2" y="3" width="16" height="11"/><path d="M4 9h3l1.5-3 2 6 1.5-4 1 1h3M10 14v3M6 17h8"/></g></symbol>
  </defs>
</svg>

<!-- Row 1 -->
<section class="slide cover" style="left:10px;top:10px">
  <svg class="art" viewBox="0 0 381 217">
    <path d="M0 0H381V150Q200 168 0 174Z" fill="url(#coverGrad)" role="img" aria-label="Dark teal technology backdrop with a hexagon network"/>
    <path d="M0 174Q200 168 381 150V156Q200 184 0 190Z" fill="var(--orange)"/>
  </svg>
  <h1 class="title">Data Management<br>as a Service</h1>
  <div class="date">12 Dec 2022</div>
  <div class="brand">TAVEXO</div>
</section>

<section class="slide cover" style="left:409px;top:10px">
  <svg class="art" viewBox="0 0 381 217">
    <rect width="381" height="179" fill="url(#coverGrad)" role="img" aria-label="Dark teal technology backdrop with a hexagon network"/>
    <rect y="179" width="381" height="3.5" fill="var(--orange)"/>
  </svg>
  <h1 class="title">Data Management<br>as a Service</h1>
  <div class="date">12 Dec 2022</div>
  <div class="brand">TAVEXO</div>
</section>

<section class="slide" style="left:808px;top:10px">
  <h2 class="slide-title">DMaas</h2>
  <div class="brand">TAVEXO</div>
  <svg class="art" viewBox="0 0 381 217">
    <text x="190" y="36" text-anchor="middle" class="s" style="font-size:5px;fill:#222">Volume of data created and replicated worldwide (source: Datasphere Research)</text>
    <text transform="rotate(-90 33 78)" x="33" y="78" text-anchor="middle" class="s" style="font-size:3.8px;font-weight:500;fill:#333">Data Volume in Zetabytes</text>
    <g class="tiny" text-anchor="end">
      <text x="50" y="110">0</text><text x="50" y="103.6">20</text><text x="50" y="97.2">40</text><text x="50" y="90.8">60</text><text x="50" y="84.4">80</text><text x="50" y="78">100</text><text x="50" y="71.6">120</text><text x="50" y="65.2">140</text><text x="50" y="58.8">160</text><text x="50" y="52.4">180</text><text x="50" y="46">200</text>
    </g>
    <polyline fill="none" stroke="var(--teal)" stroke-width="0.8" points="57,109 66.9,109 76.7,109 86.6,109 96.5,108.7 106.3,108.7 116.2,108.7 126.1,108.7 135.9,108.7 145.8,108.7 155.7,108.7 165.5,108.7 175.4,108.7 185.3,108.7 195.1,108.4 205,108.4 214.9,107.4 224.7,106.8 234.6,106.1 244.5,104.8 254.3,103.9 264.2,103.2 274.1,100.7 283.9,98.4 293.8,95.9 303.7,88.5 313.5,83.7 323.4,78 333.3,70.6 343.1,62 353,51.1"/>
    <g class="tiny" style="fill:var(--teal)" text-anchor="middle">
      <text x="57" y="107">0</text><text x="66.9" y="107">0</text><text x="76.7" y="107">0</text><text x="86.6" y="107">0</text><text x="96.5" y="106.5">1</text><text x="106.3" y="106.5">1</text><text x="116.2" y="106.5">1</text><text x="126.1" y="106.5">1</text><text x="135.9" y="106.5">1</text><text x="145.8" y="106.5">1</text><text x="155.7" y="106.5">1</text><text x="165.5" y="106.5">1</text><text x="175.4" y="106.5">1</text><text x="185.3" y="106.5">1</text><text x="195.1" y="106">2</text><text x="205" y="106">2</text><text x="214.9" y="105">5</text><text x="224.7" y="104.5">7</text><text x="234.6" y="104">9</text><text x="244.5" y="102.5">13</text><text x="254.3" y="101.5">16</text><text x="264.2" y="101">18</text><text x="272" y="98.5">26</text><text x="282" y="96">33</text><text x="291.5" y="93.5">41</text><text x="301.5" y="86.5">64</text><text x="311" y="81.5">79</text><text x="321" y="76">97</text><text x="331" y="68.5">120</text><text x="341" y="60">147</text><text x="353" y="49">181</text>
    </g>
    <g class="tiny" text-anchor="end" style="fill:#444">
      <text transform="rotate(-90 58 112)" x="58" y="112">1995</text><text transform="rotate(-90 67.9 112)" x="67.9" y="112">1996</text><text transform="rotate(-90 77.7 112)" x="77.7" y="112">1997</text><text transform="rotate(-90 87.6 112)" x="87.6" y="112">1998</text><text transform="rotate(-90 97.5 112)" x="97.5" y="112">1999</text><text transform="rotate(-90 107.3 112)" x="107.3" y="112">2000</text><text transform="rotate(-90 117.2 112)" x="117.2" y="112">2001</text><text transform="rotate(-90 127.1 112)" x="127.1" y="112">2002</text><text transform="rotate(-90 136.9 112)" x="136.9" y="112">2003</text><text transform="rotate(-90 146.8 112)" x="146.8" y="112">2004</text><text transform="rotate(-90 156.7 112)" x="156.7" y="112">2005</text><text transform="rotate(-90 166.5 112)" x="166.5" y="112">2006</text><text transform="rotate(-90 176.4 112)" x="176.4" y="112">2007</text><text transform="rotate(-90 186.3 112)" x="186.3" y="112">2008</text><text transform="rotate(-90 196.1 112)" x="196.1" y="112">2009</text><text transform="rotate(-90 206 112)" x="206" y="112">2010</text><text transform="rotate(-90 215.9 112)" x="215.9" y="112">2011</text><text transform="rotate(-90 225.7 112)" x="225.7" y="112">2012</text><text transform="rotate(-90 235.6 112)" x="235.6" y="112">2013</text><text transform="rotate(-90 245.5 112)" x="245.5" y="112">2014</text><text transform="rotate(-90 255.3 112)" x="255.3" y="112">2015</text><text transform="rotate(-90 265.2 112)" x="265.2" y="112">2016</text><text transform="rotate(-90 275.1 112)" x="275.1" y="112">2017</text><text transform="rotate(-90 284.9 112)" x="284.9" y="112">2018</text><text transform="rotate(-90 294.8 112)" x="294.8" y="112">2019</text><text transform="rotate(-90 304.7 112)" x="304.7" y="112">2020</text><text transform="rotate(-90 314.5 112)" x="314.5" y="112">2021</text><text transform="rotate(-90 324.4 112)" x="324.4" y="112">2022</text><text transform="rotate(-90 334.3 112)" x="334.3" y="112">2023</text><text transform="rotate(-90 344.1 112)" x="344.1" y="112">2024</text><text transform="rotate(-90 354 112)" x="354" y="112">2025</text>
    </g>
    <g fill="none" stroke-width="0.5" stroke-dasharray="2 1">
      <path d="M66 134H82M120 134H282M308 134H353" stroke="var(--teal)"/>
      <path d="M137 141H285M345 141H353" stroke="var(--orange)"/>
      <path d="M144 147H353" stroke="var(--teal)"/>
      <path d="M170 154H353" stroke="var(--orange)"/>
      <path d="M180 160H353" stroke="var(--teal)"/>
      <path d="M213 167H353" stroke="var(--orange)"/>
      <path d="M256 173H353" stroke="var(--teal)"/>
      <path d="M264 180H353" stroke="var(--orange)"/>
      <path d="M262 186H353" stroke="var(--teal)"/>
      <path d="M322 193H353" stroke="var(--orange)"/>
      <path d="M293 199H353" stroke="var(--teal)"/>
    </g>
    <g class="tiny" style="font-size:3.6px;fill:#333">
      <text x="35" y="135.3">UK DPA 1984</text><text x="84" y="135.3">UK DPA 1998</text><text x="283" y="135.3">UK DPA 2018</text>
      <text x="79" y="142.3">EU-US Safe Harbor</text><text x="286" y="142.3">EU-US Privacy Shield</text><text x="326" y="142.3">EU-US DPF</text>
      <text x="132" y="148.3">PERC</text><text x="152" y="155.3">ISO 27001</text><text x="164" y="161.3">PCI DSS</text><text x="203" y="168.3">SOC2</text>
      <text x="239" y="174.3">ISO 27018</text><text x="236" y="181.3">Cyber Essentials</text><text x="245" y="187.3">ISO 27017</text>
      <text x="284" y="194.3">Health Data Toolkit</text><text x="283" y="200.3">GDPR</text>
    </g>
  </svg>
  <div class="footer">Confidential do not distributed<span class="page">Page | 12</span></div>
</section>

<!-- Row 2 -->
<section class="slide" style="left:10px;top:231px">
  <h2 class="slide-title">DMaas</h2>
  <div class="brand">TAVEXO</div>
  <svg class="art" viewBox="0 0 381 217">
    <path d="M87 81H333V109H87Z" fill="#ececed"/>
    <path d="M333 77L341 95 333 113" fill="none" stroke="var(--teal)" stroke-width="1.6"/>
    <text x="208" y="98" text-anchor="middle" class="s" style="font-size:10px;fill:#8a8a8a">Application</text>
    <use href="#i-gear" x="240" y="88" width="12" height="12" class="ic"/>
    <use href="#hx" x="39" y="69" width="52" height="52" fill="#fff" stroke="var(--teal)" stroke-width="2"/>
    <text x="65" y="99" text-anchor="middle" class="s org" style="font-size:10px">DMaaS</text>
    <use href="#i-gear" x="125" y="122" width="14" height="14" class="ic"/>
    <use href="#i-gear" x="133" y="134" width="11" height="11" class="ic"/>
    <use href="#i-ai" x="207" y="124" width="24" height="24" class="ic"/>
    <use href="#i-monitor" x="293" y="124" width="22" height="22" class="ic"/>
    <g fill="var(--orange)">
      <path d="M100 161H176L173 173H97Z"/><path d="M184 161H258L255 173H181Z"/><path d="M268 161H343L340 173H265Z"/>
    </g>
    <g class="s" style="font-size:8px;fill:#fff" text-anchor="middle">
      <text x="137" y="170">Automation</text><text x="220" y="170">AI</text><text x="304" y="170">Service</text>
    </g>
  </svg>
  <div class="footer">Confidential do not distributed<span class="page">Page | 12</span></div>
</section>

<section class="slide" style="left:409px;top:231px">
  <div class="brand">TAVEXO</div>
  <svg class="art" viewBox="0 0 381 217">
    <text x="90" y="101" text-anchor="middle" style="font:700 17px Montserrat,sans-serif;fill:var(--teal)">DMaas</text>
    <g class="hex-soft">
      <use href="#hx" x="208" y="35" width="46" height="46"/>
      <use href="#hx" x="164" y="58" width="46" height="46"/>
      <use href="#hx" x="254" y="58" width="46" height="46"/>
      <use href="#hx" x="164" y="113" width="46" height="46"/>
      <use href="#hx" x="254" y="113" width="46" height="46"/>
      <use href="#hx" x="208" y="138" width="46" height="46"/>
    </g>
    <use href="#hx" x="204" y="78" width="54" height="54" fill="#fff" stroke="var(--teal)" stroke-width="1.5"/>
    <g fill="none" stroke="var(--teal)" stroke-width="1.6">
      <path d="M210 60L221 80"/><path d="M266 102L277 120"/><path d="M199 120L210 102"/><path d="M220 153L242 153"/><path d="M255 80L266 60"/>
    </g>
    <g class="s org" text-anchor="middle" style="font-size:5.5px">
      <text x="231" y="57">EDRMS</text><text x="187" y="77">Data</text><text x="187" y="83">Mapping</text>
      <text x="277" y="80">Assessment</text><text x="187" y="135">Lifecycle</text><text x="277" y="134">Classification</text><text x="231" y="160">Privacy</text>
      <text x="231" y="107" style="font-size:10px">DMaaS</text>
    </g>
    <g class="ic">
      <use href="#i-monitor" x="226" y="60" width="10" height="10"/><use href="#i-doc" x="182" y="86" width="10" height="10"/>
      <use href="#i-chart" x="272" y="84" width="10" height="10"/><use href="#i-sync" x="182" y="138" width="10" height="10"/>
      <use href="#i-search" x="272" y="138" width="10" height="10"/><use href="#i-monitor" x="226" y="163" width="10" height="10"/>
      <use href="#i-cloud" x="224" y="110" width="14" height="12"/>
    </g>
  </svg>
  <div class="footer">Confidential do not distributed<span class="page">Page | 12</span></div>
</section>

<section class="slide" style="left:808px;top:231px">
  <h2 class="slide-title">DMaas</h2>
  <div class="brand">TAVEXO</div>
  <svg class="art" viewBox="0 0 381 217">
    <g class="s" style="font-size:5.5px;fill:#222">
      <text x="20" y="77">Customer's</text><text x="20" y="84">Public Cloud</text>
      <text x="20" y="146">Customer's</text><text x="20" y="153">Premise</text>
    </g>
    <rect x="62" y="52" width="94" height="52" rx="4" fill="var(--panel)"/>
    <rect x="80" y="124" width="120" height="50" rx="4" fill="var(--panel)"/>
    <circle cx="78" cy="78" r="16" fill="var(--teal)"/><use href="#i-cloud" x="68" y="69" width="20" height="18" style="color:#fff"/>
    <circle cx="78" cy="149" r="16" fill="var(--teal)"/><use href="#i-bldg" x="69" y="140" width="18" height="18" style="color:#fff"/>
    <g class="ic">
      <use href="#i-db" x="101" y="69" width="17" height="17"/><use href="#i-doc" x="124" y="69" width="17" height="17"/>
      <use href="#i-db" x="101" y="140" width="17" height="17"/><use href="#i-doc" x="124" y="140" width="17" height="17"/>
      <rect x="169" y="140" width="16" height="16" fill="#fff" stroke="#8a8a8a" stroke-width="0.6"/><use href="#i-gear" x="171" y="142" width="12" height="12"/>
    </g>
    <path d="M145 145l3 4-3 4" fill="none" stroke="var(--teal)" stroke-width="2.2" transform="translate(5 0)"/>
    <path d="M156 78H223" stroke="var(--orange)" stroke-width="0.6"/><path d="M221 76l3 2-3 2z" fill="var(--orange)"/>
    <text x="202" y="75" class="tiny" text-anchor="middle">Metadata Reporting</text>
    <path d="M200 149H229V84" fill="none" stroke="var(--orange)" stroke-width="0.6"/><path d="M227 86l2-3 2 3z" fill="var(--orange)"/>
    <text transform="rotate(-90 234 118)" x="234" y="118" class="tiny" text-anchor="middle">Metadata Reporting</text>
    <text x="178" y="129" class="tiny" text-anchor="middle">VM / Physical Appliance</text>
    <text x="170" y="165" class="tiny">• Read source data</text><text x="170" y="169" class="tiny">• Tunnel Encryption</text>
    <path d="M237 78a9 9 0 0 1 4-13 12 12 0 0 1 22-6 9 9 0 0 1 20 5 7 7 0 0 1 0 14" fill="#fff" stroke="var(--teal)" stroke-width="1"/>
    <text x="260" y="74" text-anchor="middle" style="font:700 6.5px Montserrat,sans-serif;letter-spacing:.8px;fill:var(--ink)">TAVEXO</text>
    <g class="ic">
      <rect x="242" y="81" width="13" height="13" fill="#fff" stroke="#8a8a8a" stroke-width="0.5"/><use href="#i-gear" x="243.5" y="82.5" width="10" height="10"/>
      <rect x="264" y="81" width="13" height="13" fill="#fff" stroke="#8a8a8a" stroke-width="0.5"/><use href="#i-ai" x="265.5" y="82.5" width="10" height="10"/>
    </g>
    <text x="259" y="101" class="tiny" text-anchor="middle">Indexing and AI engine</text>
    <use href="#i-user" x="295" y="38" width="14" height="14" class="ic"/>
    <path d="M302 53V68H284" fill="none" stroke="var(--orange)" stroke-width="0.6" stroke-dasharray="1.5 1"/>
    <g fill="#c9d3db">
      <circle cx="301" cy="105" r="6"/><rect x="312" y="99" width="12" height="12" rx="1.5" fill="#2c3f6a"/><circle cx="339" cy="105" r="6" fill="#3a3a7a"/>
      <rect x="296" y="121" width="11" height="10" rx="1" fill="#7a7a7a"/>
      <rect x="295" y="140" width="14" height="10" fill="#2b55a3"/><rect x="318" y="140" width="16" height="10" fill="#2e8d4a"/>
    </g>
    <text x="309" y="125" class="tiny" style="font-size:4px;fill:#222">Cyber Assurance</text><text x="309" y="130" class="tiny" style="font-size:4px;fill:#222">Board</text>
  </svg>
  <div class="footer">Confidential do not distributed<span class="page">Page | 12</span></div>
</section>

<!-- Row 3 -->
<section class="slide" style="left:10px;top:458px">
  <h2 class="slide-title">DMaaS | Lifecycle</h2>
  <div class="brand">TAVEXO</div>
  <svg class="art" viewBox="0 0 381 217">
    <use href="#hx" x="15" y="32" width="50" height="50" class="hex-soft"/>
    <path d="M52 35L65 57" stroke="var(--teal)" stroke-width="2"/>
    <text x="40" y="58" text-anchor="middle" class="s org" style="font-size:6.5px">Lifecycle</text>
    <use href="#i-sync" x="35" y="61" width="10" height="10" class="ic"/>
    <g fill="#fff" stroke="#ececec" stroke-width="0.8">
      <rect x="52" y="90" width="89" height="97" rx="4"/><rect x="165" y="112" width="49" height="48" rx="4"/>
      <rect x="237" y="112" width="49" height="48" rx="4"/><rect x="309" y="90" width="54" height="97" rx="4"/>
    </g>
    <g class="ic">
      <use href="#i-db" x="80" y="98" width="13" height="13"/><use href="#i-cloud" x="109" y="99" width="18" height="16"/>
      <use href="#i-db" x="66" y="122" width="13" height="13"/><use href="#i-cloud" x="95" y="124" width="18" height="16"/>
      <use href="#i-cloud" x="79" y="147" width="18" height="16"/><use href="#i-db" x="112" y="149" width="13" height="13"/>
      <use href="#i-chart" x="181" y="120" width="16" height="16"/><use href="#i-in" x="253" y="120" width="16" height="16"/>
      <use href="#i-chart" x="325" y="127" width="22" height="22"/>
    </g>
    <g fill="none" stroke="var(--teal)" stroke-width="0.7">
      <path d="M148 136H160"/><path d="M220 136H232"/><path d="M292 136H304"/>
    </g>
    <g fill="var(--teal)"><path d="M160 134l3 2-3 2z"/><path d="M232 134l3 2-3 2z"/><path d="M304 134l3 2-3 2z"/></g>
    <g class="s org" text-anchor="middle" style="font-size:5.5px">
      <text x="97" y="182">Unstructured Data Siloes</text>
      <text x="190" y="146">ROT</text><text x="190" y="153">Analysis</text>
      <text x="262" y="146">Automated</text><text x="262" y="153">Remediation</text>
      <text x="336" y="101">Storage Vendor</text><text x="336" y="107">Agnostic</text>
      <text x="336" y="168">Streamlined,</text><text x="336" y="175">Controlled Data</text><text x="336" y="182">Storage</text>
    </g>
  </svg>
  <div class="footer">Confidential do not distributed<span class="page">Page | 12</span></div>
</section>

<section class="slide" style="left:409px;top:458px">
  <h2 class="slide-title">DMaaS | Privacy</h2>
  <div class="brand">TAVEXO</div>
  <svg class="art" viewBox="0 0 381 217">
    <use href="#hx" x="15" y="32" width="50" height="50" class="hex-soft"/>
    <path d="M15 57L27 79" stroke="var(--teal)" stroke-width="2"/>
    <text x="40" y="52" text-anchor="middle" class="s org" style="font-size:6.5px">Privacy</text>
    <use href="#i-monitor" x="34" y="55" width="12" height="12" class="ic"/>
    <rect x="66" y="125" width="292" height="3.5" rx="1.7" fill="#d4d5d6"/>
    <g stroke="var(--teal)" stroke-width="0.5"><path d="M100 113V124M289 113V124M146 130V146M334 130V146"/></g>
    <g stroke="var(--orange)" stroke-width="0.5"><path d="M195 113V124M240 130V146"/></g>
    <use href="#hp" x="81" y="75" width="38" height="38" fill="var(--teal)"/>
    <use href="#hp" x="176" y="75" width="38" height="38" fill="var(--orange)"/>
    <use href="#hp" x="270" y="75" width="38" height="38" fill="var(--teal)"/>
    <use href="#hp" x="127" y="147" width="38" height="38" fill="var(--teal)"/>
    <use href="#hp" x="221" y="147" width="38" height="38" fill="var(--orange)"/>
    <use href="#hp" x="315" y="147" width="38" height="38" fill="var(--teal)"/>
    <g fill="#fff"><circle cx="100" cy="94" r="10"/><circle cx="195" cy="94" r="10"/><circle cx="289" cy="94" r="10"/><circle cx="146" cy="166" r="10"/><circle cx="240" cy="166" r="10"/><circle cx="334" cy="166" r="10"/></g>
    <use href="#i-monitor" x="93" y="87" width="14" height="14" style="color:var(--teal)"/>
    <use href="#i-db" x="188" y="87" width="14" height="14" style="color:var(--orange)"/>
    <use href="#i-user" x="282" y="87" width="14" height="14" style="color:var(--teal)"/>
    <use href="#i-search" x="139" y="159" width="14" height="14" style="color:var(--teal)"/>
    <use href="#i-sync" x="233" y="159" width="14" height="14" style="color:var(--orange)"/>
    <use href="#i-export" x="327" y="159" width="14" height="14" style="color:var(--teal)"/>
    <g class="ic">
      <use href="#i-user" x="132" y="94" width="8" height="8"/><use href="#i-user" x="139" y="94" width="8" height="8"/><use href="#i-user" x="146" y="94" width="8" height="8"/>
      <use href="#i-user" x="226" y="94" width="8" height="8"/><use href="#i-user" x="233" y="94" width="8" height="8"/><use href="#i-user" x="240" y="94" width="8" height="8"/>
      <use href="#i-user" x="330" y="94" width="8" height="8"/><use href="#i-user" x="96" y="144" width="8" height="8"/>
      <use href="#i-user" x="280" y="152" width="7" height="7"/><use href="#i-user" x="286" y="152" width="7" height="7"/><use href="#i-user" x="292" y="152" width="7" height="7"/>
      <use href="#i-user" x="277" y="158" width="7" height="7"/><use href="#i-user" x="283" y="158" width="7" height="7"/><use href="#i-user" x="289" y="158" width="7" height="7"/><use href="#i-user" x="295" y="158" width="7" height="7"/>
    </g>
    <g class="lbl" text-anchor="middle" style="font-size:5.5px">
      <text x="146" y="110">E-discovery &amp;</text><text x="146" y="117">Collection</text>
      <text x="240" y="110">Conversion</text><text x="334" y="110">Export</text>
      <text x="100" y="141">ID Check</text><text x="195" y="141">Collection Silo</text>
      <text x="289" y="141">Manual</text><text x="289" y="148">Redaction</text>
    </g>
    <rect x="66" y="188" width="292" height="11" fill="#e4e5e6"/>
    <use href="#i-user" x="176" y="190" width="7" height="7" class="ic"/>
    <text x="225" y="196" class="s" text-anchor="middle" style="font-size:5.5px;fill:#333">Manual process management</text>
  </svg>
  <div class="footer">Confidential do not distributed<span class="page">Page | 12</span></div>
</section>

<section class="slide" style="left:808px;top:458px">
  <h2 class="slide-title">DMaaS | Privacy</h2>
  <div class="brand">TAVEXO</div>
  <svg class="art" viewBox="0 0 381 217">
    <use href="#hx" x="15" y="32" width="50" height="50" class="hex-soft"/>
    <path d="M15 57L27 79" stroke="var(--teal)" stroke-width="2"/>
    <text x="40" y="52" text-anchor="middle" class="s org" style="font-size:6.5px">Privacy</text>
    <use href="#i-monitor" x="34" y="55" width="12" height="12" class="ic"/>
    <text x="231" y="66" text-anchor="middle" class="s" style="font-size:6px;fill:#222">Software</text>
    <text x="231" y="73" text-anchor="middle" class="s" style="font-size:6px;fill:#222">Automation</text>
    <rect x="115" y="90" width="232" height="84" fill="none" stroke="#cfcfcf" stroke-width="0.6" stroke-dasharray="2 1.5"/>
    <circle cx="231" cy="90" r="10" fill="#fff"/>
    <use href="#i-sync" x="222" y="81" width="18" height="18" class="ic"/>
    <g fill="#fff" stroke="#ececec" stroke-width="0.8">
      <rect x="47" y="113" width="49" height="49" rx="4"/><rect x="128" y="113" width="49" height="49" rx="4"/>
      <rect x="207" y="113" width="49" height="49" rx="4"/><rect x="286" y="113" width="49" height="49" rx="4"/>
    </g>
    <g class="ic">
      <use href="#i-monitor" x="63" y="120" width="17" height="17"/><use href="#i-search" x="144" y="120" width="17" height="17"/>
      <use href="#i-ai" x="223" y="120" width="17" height="17"/><use href="#i-export" x="302" y="120" width="17" height="17"/>
    </g>
    <g fill="none" stroke="var(--teal)" stroke-width="0.6"><path d="M100 137H124M181 137H203M260 137H282"/></g>
    <g fill="var(--teal)"><path d="M124 135l3 2-3 2z"/><path d="M203 135l3 2-3 2z"/><path d="M282 135l3 2-3 2z"/></g>
    <g class="lbl" text-anchor="middle" style="font-size:5.5px">
      <text x="71" y="148">ID Check</text><text x="152" y="148">E-discovery &amp;</text><text x="152" y="155">Collection</text>
      <text x="231" y="148">Redaction</text><text x="310" y="148">Export</text>
    </g>
    <rect x="46" y="187" width="301" height="11" fill="#e4e5e6"/>
    <use href="#i-user" x="130" y="189" width="7" height="7" class="ic"/>
    <text x="198" y="195" class="s" text-anchor="middle" style="font-size:5.5px;fill:#333">Self service or managed request workflow</text>
  </svg>
  <div class="footer">Confidential do not distributed<span class="page">Page | 12</span></div>
</section>

<!-- Row 4 -->
<section class="slide" style="left:10px;top:685px">
  <div class="brand" style="right:26px">TAVEXO</div>
  <svg class="art" viewBox="0 0 381 217">
    <use href="#hx" x="41" y="50" width="68" height="68" class="hex-soft"/>
    <text x="75" y="81" text-anchor="middle" class="s org" style="font-size:7px">Redaction</text>
    <use href="#i-monitor" x="66" y="85" width="18" height="18" class="ic"/>
    <rect x="146" y="18" width="127" height="183" fill="#fff" stroke="#9a9a9a" stroke-width="0.6"/>
    <text x="150" y="26" class="s" style="font-size:6px;font-weight:700;fill:#2b7d2b">Automated Redaction</text>
    <rect x="150" y="31" width="119" height="166" class="doc-placeholder" role="img" aria-label="Sample letter with sensitive details highlighted in green for automated redaction"/>
  </svg>
  <div class="footer">Confidential do not distributed<span class="page">Page | 12</span></div>
</section>

<section class="slide" style="left:409px;top:685px">
  <div class="brand" style="right:26px">TAVEXO</div>
  <svg class="art" viewBox="0 0 381 217">
    <use href="#hx" x="41" y="50" width="68" height="68" class="hex-soft"/>
    <text x="75" y="81" text-anchor="middle" class="s org" style="font-size:7px">Redaction</text>
    <use href="#i-monitor" x="66" y="85" width="18" height="18" class="ic"/>
    <rect x="146" y="18" width="127" height="183" fill="#fff" stroke="#9a9a9a" stroke-width="0.6"/>
    <text x="150" y="26" class="s" style="font-size:6px;font-weight:700;fill:#222">Immutable Redaction</text>
    <rect x="150" y="31" width="119" height="166" class="doc-placeholder" role="img" aria-label="Sample letter with sensitive details blacked out by immutable redaction"/>
  </svg>
  <div class="footer">Confidential do not distributed<span class="page">Page | 12</span></div>
</section>

<section class="slide" style="left:808px;top:685px">
  <h2 class="slide-title">DMaaS | Privacy</h2>
  <div class="brand">TAVEXO</div>
  <svg class="art" viewBox="0 0 381 217">
    <use href="#hx" x="15" y="38" width="68" height="68" class="hex-soft"/>
    <text x="49" y="66" text-anchor="middle" class="s org" style="font-size:7px">Redaction</text>
    <use href="#i-monitor" x="40" y="70" width="18" height="18" class="ic"/>
    <rect x="95" y="99" width="193" height="65" fill="none" stroke="#cfcfcf" stroke-width="0.6" stroke-dasharray="2 1.5"/>
    <g fill="#fff" stroke="#ececec" stroke-width="0.8"><rect x="26" y="108" width="48" height="48" rx="4"/><rect x="306" y="108" width="50" height="48" rx="4"/></g>
    <g class="ic">
      <use href="#i-search" x="41" y="112" width="17" height="17"/>
      <use href="#i-in" x="114" y="111" width="16" height="16"/><use href="#i-doc" x="160" y="111" width="16" height="16"/>
      <use href="#i-sync" x="207" y="111" width="16" height="16"/><use href="#i-ai" x="253" y="111" width="16" height="16"/>
      <use href="#i-export" x="323" y="112" width="17" height="17"/>
    </g>
    <g fill="none" stroke="var(--teal)" stroke-width="0.6"><path d="M76 129H108M272 129H300"/></g>
    <g fill="var(--teal)"><path d="M108 127l3 2-3 2z"/><path d="M300 127l3 2-3 2z"/></g>
    <g class="lbl" text-anchor="middle" style="font-size:5.5px;fill:#333">
      <text x="50" y="138">E-discovery &amp;</text><text x="50" y="145">Collection</text>
      <text x="122" y="141">Ingestion</text><text x="168" y="141">Deduplication</text><text x="215" y="141">Conversion</text><text x="261" y="141">Redaction</text>
      <text x="331" y="141">Export</text>
    </g>
    <path d="M261 184V149" stroke="var(--orange)" stroke-width="0.8"/><path d="M259 150l2-3 2 3z" fill="var(--orange)"/>
    <use href="#i-user" x="230" y="184" width="10" height="10" class="ic"/>
    <text x="261" y="192" class="s" text-anchor="middle" style="font-size:5.5px;fill:#222">QA Check</text>
  </svg>
  <div class="footer">Confidential do not distributed<span class="page">Page | 12</span></div>
</section>

<!-- Row 5 -->
<section class="slide" style="left:10px;top:911px">
  <h2 class="slide-title">DMaaS | Privacy</h2>
  <div class="brand" style="right:26px">TAVEXO</div>
  <svg class="art" viewBox="0 0 381 217">
    <use href="#hx" x="15" y="30" width="50" height="50" class="hex-soft"/>
    <path d="M15 55L27 77" stroke="var(--teal)" stroke-width="2"/>
    <text x="40" y="50" text-anchor="middle" class="s org" style="font-size:6.5px">Privacy</text>
    <use href="#i-monitor" x="34" y="53" width="12" height="12" class="ic"/>
    <rect x="19" y="87" width="199" height="114" rx="6" fill="var(--panel)"/>
    <rect x="266" y="87" width="92" height="114" rx="6" fill="var(--panel)"/>
    <rect x="28" y="140" width="169" height="2" fill="#cdd0d2"/>
    <g stroke="var(--teal)" stroke-width="0.4"><path d="M47 132V139M156 132V139M74 143V152M184 143V152"/></g>
    <g stroke="var(--orange)" stroke-width="0.4"><path d="M102 132V139M129 143V152"/></g>
    <use href="#hp" x="36" y="110" width="22" height="22" fill="var(--teal)"/><use href="#hp" x="91" y="110" width="22" height="22" fill="var(--orange)"/><use href="#hp" x="145" y="110" width="22" height="22" fill="var(--teal)"/>
    <use href="#hp" x="63" y="152" width="22" height="22" fill="var(--teal)"/><use href="#hp" x="118" y="152" width="22" height="22" fill="var(--orange)"/><use href="#hp" x="173" y="152" width="22" height="22" fill="var(--teal)"/>
    <g fill="#fff"><circle cx="47" cy="121" r="6"/><circle cx="102" cy="121" r="6"/><circle cx="156" cy="121" r="6"/><circle cx="74" cy="163" r="6"/><circle cx="129" cy="163" r="6"/><circle cx="184" cy="163" r="6"/></g>
    <g class="tiny" text-anchor="middle">
      <text x="74" y="131">E-discovery &amp;</text><text x="74" y="135">Collection</text><text x="129" y="132">Conversion</text><text x="184" y="132">Export</text>
      <text x="47" y="150">ID Check</text><text x="102" y="150">Collection Silo</text><text x="156" y="149">Manual</text><text x="156" y="153">Redaction</text>
    </g>
    <rect x="28" y="181" width="169" height="5" fill="#dcdedf"/>
    <text x="115" y="185" class="tiny" text-anchor="middle" style="fill:#333">Manual process management</text>
    <path d="M222 144H266" stroke="var(--teal)" stroke-width="0.8"/><path d="M265 142l3 2-3 2z" fill="var(--teal)"/>
    <use href="#i-sync" x="283" y="104" width="16" height="16" style="color:var(--orange)"/>
    <use href="#i-ai" x="283" y="139" width="16" height="16" style="color:var(--orange)"/>
    <use href="#i-gear" x="283" y="175" width="16" height="16" style="color:var(--orange)"/>
    <g class="s" style="font-size:6px;fill:#333"><text x="307" y="114">Automation</text><text x="307" y="149">AI</text><text x="307" y="185">Service</text></g>
  </svg>
  <div class="footer">Confidential do not distributed<span class="page">Page | 12</span></div>
</section>

<section class="slide" style="left:409px;top:911px">
  <h2 class="slide-title">DMaaS | Assessment</h2>
  <div class="brand" style="right:26px">TAVEXO</div>
  <svg class="art" viewBox="0 0 381 217">
    <use href="#hx" x="20" y="30" width="50" height="50" class="hex-soft"/>
    <path d="M20 55L32 77" stroke="var(--teal)" stroke-width="2"/>
    <text x="45" y="52" text-anchor="middle" class="s org" style="font-size:5.5px">Assessment</text>
    <use href="#i-chart" x="39" y="55" width="12" height="12" class="ic"/>
    <g class="s" style="font-size:6px;fill:#777">
      <text x="30" y="105" style="font-weight:700;fill:var(--orange)">Packaged</text>
      <text x="38" y="117">Data centric storage refresh or cloud migration</text>
      <text x="38" y="129">readiness assessment</text>
      <text x="38" y="140">Data Owner and Data Access Assessment</text>
      <text x="38" y="152">Data Classification and Sensitivity Assessment</text>
      <text x="30" y="176" style="font-weight:700;fill:var(--orange)">Generic</text>
      <text x="38" y="188">Data Management Assessment</text>
    </g>
    <g fill="var(--orange)"><rect x="30" y="114" width="2" height="2"/><rect x="30" y="137" width="2" height="2"/><rect x="30" y="149" width="2" height="2"/><rect x="30" y="185" width="2" height="2"/></g>
    <rect x="185" y="36" width="109" height="64" fill="url(#reportDark)" role="img" aria-label="Data age assessment report page with bar and pie charts"/>
    <rect x="185" y="123" width="109" height="62" fill="url(#reportDark)" role="img" aria-label="Sensitive data assessment report page with charts and summary tables"/>
    <rect x="299" y="83" width="70" height="65" fill="#ececec" role="img" aria-label="Radar chart scoring security, usage, compliance and storage"/>
  </svg>
  <div class="footer">Confidential do not distributed<span class="page">Page | 12</span></div>
</section>

<section class="slide thanks" style="left:808px;top:911px">
  <svg class="art" viewBox="0 0 381 217" role="img" aria-label="Faint hexagon network texture over teal">
    <rect width="381" height="168" fill="var(--teal)"/>
    <rect y="168" width="381" height="4" fill="var(--orange)"/>
    <rect y="172" width="381" height="45" fill="#fff"/>
  </svg>
  <div class="big">Thank you</div>
  <div class="pill">TAVEXO</div>
  <div class="contacts">
    <span>www.tavexo.com</span><span>+44 20 7946 0183</span><span>14 Harbour Lane, Leeds</span><span>hello@tavexo.com</span>
  </div>
</section>

</div>
</body>
</html>
```